Flavour Wheel - Illustrator Graph

I need my basic layout, from the sample I provided, turned into a professional looking flavour wheel.

I have attached a sample of a final design I like, but please use your own creativity also.

All the exact words I need are on the uploaded illustration.

I would need the file supplied to me in .ai

Industry/Entity Type

Wheel

Font styles to use
Sans Serif

Colors

Designer to choose colors to be used in the design.

Requirements
Must have
• Files must be supplied in .ai format with fonts not outlined.
• I need each segment separated so I can change the colours if needed myself.
Nice to have
• I like small white gaps between the sections.

```html
<!DOCTYPE html>
<html lang="en">
<head>
<meta charset="utf-8">
<title>Flavour Wheel</title>
<link rel="stylesheet" href="https://fonts.googleapis.com/css2?family=Ubuntu:wght@400;500&display=swap">
<style>
  :root {
    --bg: #f7f7f7;
    --gap: #ffffff;
    --ink: #1d3b3f;
    --ink-light: #ffffff;

    --sour: #e8b012; --earthy: #c94a30; --sweet: #e55a30; --salty: #e6e6e6;
    --savoury: #772432; --spicy: #ee3438; --smokey: #a57a63;

    --bitter: #6b3a26; --vinegary: #b09334; --citrus: #a2ad2a; --floral: #d6106c;
    --herby: #38a153; --nutty: #8a6a4e; --buttery: #f6edc0; --fruity-sweet: #f4a32a;
    --sugary: #cbcbcb; --caramel: #d07530; --charred: #4a2618; --briney: #ececda;
    --meatiness: #cccc33; --umami: #780604; --chilli: #fe0000; --peppery: #333333;
    --cajun: #fe0a6e; --woody: #b55a2e; --fruity-smoke: #ffcc00; --acrid: #ffff66;
  }
  html, body { margin: 0; padding: 0; overflow: hidden; background: var(--bg); }
  .canvas { width: 1200px; height: 1146px; position: relative; background: var(--bg); }
  .wheel { display: block; }
  .wheel text { font-family: "Ubuntu", sans-serif; dominant-baseline: central; }
  .seg { fill: none; }
  .divider { stroke: var(--gap); stroke-width: 3; }
  .ring-edge { fill: none; stroke: var(--gap); stroke-width: 3; }
  .family-label { font-size: 19px; fill: var(--ink-light); text-anchor: middle; }
  .note-label { font-size: 18px; fill: var(--ink-light); text-anchor: middle; }
  .dark { fill: var(--ink); }
  .leaf { font-size: 18.5px; fill: var(--ink); }
  .leaf.left { text-anchor: end; }
  .leaf.faint { fill: #eeeeee; }
</style>
</head>
<body>
<div class="canvas">
<svg class="wheel" width="1200" height="1146" viewBox="0 0 1500 1432.5" xmlns="http://www.w3.org/2000/svg" role="img" aria-label="Flavour wheel">
<g transform="translate(733 731)">

  <!-- flavour families (inner ring) -->
  <g class="ring-families" transform="rotate(-90)">
    <circle class="seg" r="116" stroke-width="122" pathLength="360" stroke="var(--sour)" stroke-dasharray="49 311" stroke-dashoffset="23"/>
    <circle class="seg" r="116" stroke-width="122" pathLength="360" stroke="var(--earthy)" stroke-dasharray="68 292" stroke-dashoffset="-26"/>
    <circle class="seg" r="116" stroke-width="122" pathLength="360" stroke="var(--sweet)" stroke-dasharray="48 312" stroke-dashoffset="-94"/>
    <circle class="seg" r="116" stroke-width="122" pathLength="360" stroke="var(--salty)" stroke-dasharray="38 322" stroke-dashoffset="-142"/>
    <circle class="seg" r="116" stroke-width="122" pathLength="360" stroke="var(--savoury)" stroke-dasharray="42 318" stroke-dashoffset="-180"/>
    <circle class="seg" r="116" stroke-width="122" pathLength="360" stroke="var(--spicy)" stroke-dasharray="56 304" stroke-dashoffset="-222"/>
    <circle class="seg" r="116" stroke-width="122" pathLength="360" stroke="var(--smokey)" stroke-dasharray="59 301" stroke-dashoffset="-278"/>
  </g>

  <!-- flavour notes (outer ring) -->
  <g class="ring-notes" transform="rotate(-90)">
    <circle class="seg" r="257" stroke-width="160" pathLength="360" stroke="var(--woody)" stroke-dasharray="12 348" stroke-dashoffset="-278"/>
    <circle class="seg" r="257" stroke-width="160" pathLength="360" stroke="var(--fruity-smoke)" stroke-dasharray="17 343" stroke-dashoffset="-290"/>
    <circle class="seg" r="257" stroke-width="160" pathLength="360" stroke="var(--acrid)" stroke-dasharray="16 344" stroke-dashoffset="-307"/>
    <circle class="seg" r="257" stroke-width="160" pathLength="360" stroke="var(--bitter)" stroke-dasharray="23.5 336.5" stroke-dashoffset="-323"/>
    <circle class="seg" r="257" stroke-width="160" pathLength="360" stroke="var(--vinegary)" stroke-dasharray="20.5 339.5" stroke-dashoffset="13.5"/>
    <circle class="seg" r="257" stroke-width="160" pathLength="360" stroke="var(--citrus)" stroke-dasharray="15 345" stroke-dashoffset="-7"/>
    <circle class="seg" r="257" stroke-width="160" pathLength="360" stroke="var(--floral)" stroke-dasharray="24 336" stroke-dashoffset="-22"/>
    <circle class="seg" r="257" stroke-width="160" pathLength="360" stroke="var(--herby)" stroke-dasharray="22 338" stroke-dashoffset="-46"/>
    <circle class="seg" r="257" stroke-width="160" pathLength="360" stroke="var(--nutty)" stroke-dasharray="10 350" stroke-dashoffset="-68"/>
    <circle class="seg" r="257" stroke-width="160" pathLength="360" stroke="var(--buttery)" stroke-dasharray="12 348" stroke-dashoffset="-78"/>
    <circle class="seg" r="257" stroke-width="160" pathLength="360" stroke="var(--fruity-sweet)" stroke-dasharray="10.5 349.5" stroke-dashoffset="-90"/>
    <circle class="seg" r="257" stroke-width="160" pathLength="360" stroke="var(--sugary)" stroke-dasharray="12.9 347.1" stroke-dashoffset="-100.5"/>
    <circle class="seg" r="257" stroke-width="160" pathLength="360" stroke="var(--caramel)" stroke-dasharray="14.6 345.4" stroke-dashoffset="-113.4"/>
    <circle class="seg" r="257" stroke-width="160" pathLength="360" stroke="var(--charred)" stroke-dasharray="28 332" stroke-dashoffset="-128"/>
    <circle class="seg" r="257" stroke-width="160" pathLength="360" stroke="var(--briney)" stroke-dasharray="24 336" stroke-dashoffset="-156"/>
    <circle class="seg" r="257" stroke-width="160" pathLength="360" stroke="var(--meatiness)" stroke-dasharray="24 336" stroke-dashoffset="-180"/>
    <circle class="seg" r="257" stroke-width="160" pathLength="360" stroke="var(--umami)" stroke-dasharray="21 339" stroke-dashoffset="-204"/>
    <circle class="seg" r="257" stroke-width="160" pathLength="360" stroke="var(--chilli)" stroke-dasharray="21 339" stroke-dashoffset="-225"/>
    <circle class="seg" r="257" stroke-width="160" pathLength="360" stroke="var(--peppery)" stroke-dasharray="18 342" stroke-dashoffset="-246"/>
    <circle class="seg" r="257" stroke-width="160" pathLength="360" stroke="var(--cajun)" stroke-dasharray="14 346" stroke-dashoffset="-264"/>
  </g>

  <!-- white gaps -->
  <g class="gaps">
    <circle class="ring-edge" r="55"/>
    <circle class="ring-edge" r="177"/>
    <line class="divider" x1="0" y1="-54" x2="0" y2="-178" transform="rotate(-23)"/>
    <line class="divider" x1="0" y1="-54" x2="0" y2="-178" transform="rotate(26)"/>
    <line class="divider" x1="0" y1="-54" x2="0" y2="-178" transform="rotate(94)"/>
    <line class="divider" x1="0" y1="-54" x2="0" y2="-178" transform="rotate(142)"/>
    <line class="divider" x1="0" y1="-54" x2="0" y2="-178" transform="rotate(180)"/>
    <line class="divider" x1="0" y1="-54" x2="0" y2="-178" transform="rotate(222)"/>
    <line class="divider" x1="0" y1="-54" x2="0" y2="-178" transform="rotate(278)"/>

    <line class="divider" x1="0" y1="-176" x2="0" y2="-338" transform="rotate(278)"/>
    <line class="divider" x1="0" y1="-176" x2="0" y2="-338" transform="rotate(290)"/>
    <line class="divider" x1="0" y1="-176" x2="0" y2="-338" transform="rotate(307)"/>
    <line class="divider" x1="0" y1="-176" x2="0" y2="-338" transform="rotate(323)"/>
    <line class="divider" x1="0" y1="-176" x2="0" y2="-338" transform="rotate(346.5)"/>
    <line class="divider" x1="0" y1="-176" x2="0" y2="-338" transform="rotate(7)"/>
    <line class="divider" x1="0" y1="-176" x2="0" y2="-338" transform="rotate(22)"/>
    <line class="divider" x1="0" y1="-176" x2="0" y2="-338" transform="rotate(46)"/>
    <line class="divider" x1="0" y1="-176" x2="0" y2="-338" transform="rotate(68)"/>
    <line class="divider" x1="0" y1="-176" x2="0" y2="-338" transform="rotate(78)"/>
    <line class="divider" x1="0" y1="-176" x2="0" y2="-338" transform="rotate(90)"/>
    <line class="divider" x1="0" y1="-176" x2="0" y2="-338" transform="rotate(100.5)"/>
    <line class="divider" x1="0" y1="-176" x2="0" y2="-338" transform="rotate(113.4)"/>
    <line class="divider" x1="0" y1="-176" x2="0" y2="-338" transform="rotate(128)"/>
    <line class="divider" x1="0" y1="-176" x2="0" y2="-338" transform="rotate(156)"/>
    <line class="divider" x1="0" y1="-176" x2="0" y2="-338" transform="rotate(180)"/>
    <line class="divider" x1="0" y1="-176" x2="0" y2="-338" transform="rotate(204)"/>
    <line class="divider" x1="0" y1="-176" x2="0" y2="-338" transform="rotate(225)"/>
    <line class="divider" x1="0" y1="-176" x2="0" y2="-338" transform="rotate(246)"/>
    <line class="divider" x1="0" y1="-176" x2="0" y2="-338" transform="rotate(264)"/>
  </g>

  <!-- family labels -->
  <g class="family-labels">
    <text class="family-label" transform="rotate(91.5) translate(-116 0)">Sour</text>
    <text class="family-label" transform="rotate(-30) translate(116 0)">Earthy</text>
    <text class="family-label" transform="rotate(28) translate(116 0)">Sweet</text>
    <text class="family-label dark" transform="rotate(71) translate(116 0)">Salty</text>
    <text class="family-label" transform="rotate(291) translate(-116 0)">Savoury</text>
    <text class="family-label" transform="rotate(340) translate(-116 0)">Spicy</text>
    <text class="family-label" transform="rotate(37.5) translate(-116 0)">Smokey</text>
  </g>

  <!-- note labels -->
  <g class="note-labels">
    <text class="note-label" transform="rotate(14) translate(-257 0)">Woody</text>
    <text class="note-label" transform="rotate(28.5) translate(-257 0)">Fruity</text>
    <text class="note-label dark" transform="rotate(45) translate(-257 0)">Acrid</text>
    <text class="note-label" transform="rotate(64.75) translate(-257 0)">Bitter</text>
    <text class="note-label" transform="rotate(86.75) translate(-257 0)">Vinegary</text>
    <text class="note-label" transform="rotate(-75.5) translate(257 0)">Citrus</text>
    <text class="note-label" transform="rotate(-56) translate(257 0)">Floral</text>
    <text class="note-label" transform="rotate(-33) translate(257 0)">Herby</text>
    <text class="note-label" transform="rotate(-17) translate(257 0)">Nutty</text>
    <text class="note-label dark" transform="rotate(-6) translate(257 0)">Buttery</text>
    <text class="note-label" transform="rotate(5.25) translate(257 0)">Fruity</text>
    <text class="note-label dark" transform="rotate(17) translate(257 0)">Sugary</text>
    <text class="note-label" transform="rotate(30.7) translate(257 0)">Caramel</text>
    <text class="note-label" transform="rotate(52) translate(257 0)">Charred</text>
    <text class="note-label dark" transform="rotate(78) translate(257 0)">Briney</text>
    <text class="note-label" transform="rotate(102) translate(257 0)">Meatiness</text>
    <text class="note-label" transform="rotate(304.5) translate(-257 0)">Umami</text>
    <text class="note-label" transform="rotate(325.5) translate(-257 0)">Chilli</text>
    <text class="note-label" transform="rotate(345) translate(-257 0)">Peppery</text>
    <text class="note-label" transform="rotate(1) translate(-257 0)">Cajun</text>
  </g>

  <!-- ingredient chips -->
  <g class="chips">
    <rect x="-10" y="-362" width="20" height="20" fill="#f9a11b" transform="rotate(355)"/>
    <rect x="-10" y="-362" width="20" height="20" fill="#ef5f73" transform="rotate(358.5)"/>
    <rect x="-10" y="-362" width="20" height="20" fill="#f6efbd" transform="rotate(2.3)"/>
    <rect x="-10" y="-362" width="20" height="20" fill="#3a0010" transform="rotate(6.5)"/>
    <rect x="-10" y="-362" width="20" height="20" fill="#d81d63" transform="rotate(10.4)"/>
    <rect x="-10" y="-362" width="20" height="20" fill="#6b63b0" transform="rotate(14.05)"/>
    <rect x="-10" y="-362" width="20" height="20" fill="#e85a6e" transform="rotate(17.7)"/>
    <rect x="-10" y="-362" width="20" height="20" fill="#b24e7a" transform="rotate(21.35)"/>
    <rect x="-10" y="-362" width="20" height="20" fill="#df9466" transform="rotate(25)"/>
    <rect x="-10" y="-362" width="20" height="20" fill="#e8344e" transform="rotate(28.65)"/>
    <rect x="-10" y="-362" width="20" height="20" fill="#f4a032" transform="rotate(32.3)"/>
    <rect x="-10" y="-362" width="20" height="20" fill="#a9b53a" transform="rotate(35.95)"/>
    <rect x="-10" y="-362" width="20" height="20" fill="#4db848" transform="rotate(39.6)"/>
    <rect x="-10" y="-362" width="20" height="20" fill="#f28a5c" transform="rotate(43.25)"/>
    <rect x="-10" y="-362" width="20" height="20" fill="#c1a538" transform="rotate(46.9)"/>
    <rect x="-10" y="-362" width="20" height="20" fill="#ec5a5a" transform="rotate(50.55)"/>
    <rect x="-10" y="-362" width="20" height="20" fill="#e0601e" transform="rotate(54.2)"/>
    <rect x="-10" y="-362" width="20" height="20" fill="#ffd700" transform="rotate(57.85)"/>
    <rect x="-10" y="-362" width="20" height="20" fill="#88b040" transform="rotate(61.5)"/>
    <rect x="-10" y="-362" width="20" height="20" fill="#a19c26" transform="rotate(65.15)"/>
    <rect x="-10" y="-362" width="20" height="20" fill="#aabf94" transform="rotate(68.8)"/>
    <rect x="-10" y="-362" width="20" height="20" fill="#d6b24a" transform="rotate(72.45)"/>
    <rect x="-10" y="-362" width="20" height="20" fill="#a9cf70" transform="rotate(76.1)"/>
    <rect x="-10" y="-362" width="20" height="20" fill="#f8ec00" transform="rotate(79.75)"/>
    <rect x="-10" y="-362" width="20" height="20" fill="#c9b916" transform="rotate(83.4)"/>
    <rect x="-10" y="-362" width="20" height="20" fill="#8a1a4a" transform="rotate(87.05)"/>
    <rect x="-10" y="-362" width="20" height="20" fill="#b84040" transform="rotate(90.7)"/>
    <rect x="-10" y="-362" width="20" height="20" fill="#b8943a" transform="rotate(94.35)"/>
    <rect x="-10" y="-362" width="20" height="20" fill="#8b6344" transform="rotate(98)"/>
    <rect x="-10" y="-362" width="20" height="20" fill="#8b4a1a" transform="rotate(104.9)"/>
    <rect x="-10" y="-362" width="20" height="20" fill="#c48a6a" transform="rotate(108.3)"/>
    <rect x="-10" y="-362" width="20" height="20" fill="#e4bf80" transform="rotate(111.8)"/>
    <rect x="-10" y="-362" width="20" height="20" fill="#e05a20" transform="rotate(121.9)"/>
    <rect x="-10" y="-362" width="20" height="20" fill="#e08a20" transform="rotate(125.7)"/>
    <rect x="-10" y="-362" width="20" height="20" fill="#b83222" transform="rotate(129)"/>
    <rect x="-10" y="-362" width="20" height="20" fill="#9ccb6a" transform="rotate(146.6)"/>
    <rect x="-10" y="-362" width="20" height="20" fill="#e6e6e6" transform="rotate(150)"/>
    <rect x="-10" y="-362" width="20" height="20" fill="#c8c8c8" transform="rotate(153.6)"/>
    <rect x="-10" y="-362" width="20" height="20" fill="#053a3a" transform="rotate(157)"/>
    <rect x="-10" y="-362" width="20" height="20" fill="#cccc33" transform="rotate(174.5)"/>
    <rect x="-10" y="-362" width="20" height="20" fill="#9ccf9a" transform="rotate(178)"/>
    <rect x="-10" y="-362" width="20" height="20" fill="#f99a9a" transform="rotate(182)"/>
    <rect x="-10" y="-362" width="20" height="20" fill="#c86a9a" transform="rotate(185.9)"/>
    <rect x="-10" y="-362" width="20" height="20" fill="#cccc33" transform="rotate(197.1)"/>
    <rect x="-10" y="-362" width="20" height="20" fill="#cc99ff" transform="rotate(200.6)"/>
    <rect x="-10" y="-362" width="20" height="20" fill="#c06ac8" transform="rotate(204.1)"/>
    <rect x="-10" y="-362" width="20" height="20" fill="#6a3a9a" transform="rotate(207.7)"/>
    <rect x="-10" y="-362" width="20" height="20" fill="#99ff99" transform="rotate(211.4)"/>
    <rect x="-10" y="-362" width="20" height="20" fill="#9a3acc" transform="rotate(225.1)"/>
    <rect x="-10" y="-362" width="20" height="20" fill="#9a6a9a" transform="rotate(228.7)"/>
    <rect x="-10" y="-362" width="20" height="20" fill="#808080" transform="rotate(232.2)"/>
    <rect x="-10" y="-362" width="20" height="20" fill="#ccffcc" transform="rotate(235.5)"/>
    <rect x="-10" y="-362" width="20" height="20" fill="#ccff66" transform="rotate(239)"/>
    <rect x="-10" y="-362" width="20" height="20" fill="#cc33ff" transform="rotate(242.6)"/>
    <rect x="-10" y="-362" width="20" height="20" fill="#ee3438" transform="rotate(249.7)"/>
    <rect x="-10" y="-362" width="20" height="20" fill="#a57a63" transform="rotate(253.2)"/>
    <rect x="-10" y="-362" width="20" height="20" fill="#c84a3a" transform="rotate(256.7)"/>
    <rect x="-10" y="-362" width="20" height="20" fill="#4a2618" transform="rotate(260.2)"/>
    <rect x="-10" y="-362" width="20" height="20" fill="#053a3a" transform="rotate(263.6)"/>
    <rect x="-10" y="-362" width="20" height="20" fill="#5f9a98" transform="rotate(267)"/>
    <rect x="-10" y="-362" width="20" height="20" fill="#3300cc" transform="rotate(269.4)"/>
    <rect x="-10" y="-362" width="20" height="20" fill="#336699" transform="rotate(285)"/>
    <rect x="-10" y="-362" width="20" height="20" fill="#663333" transform="rotate(288.3)"/>
    <rect x="-10" y="-362" width="20" height="20" fill="#053a2a" transform="rotate(291.8)"/>
    <rect x="-10" y="-362" width="20" height="20" fill="#ff0000" transform="rotate(295.4)"/>
    <rect x="-10" y="-362" width="20" height="20" fill="#2e8b57" transform="rotate(298.9)"/>
    <rect x="-10" y="-362" width="20" height="20" fill="#6aaa3a" transform="rotate(316.5)"/>
    <rect x="-10" y="-362" width="20" height="20" fill="#ff3399" transform="rotate(330.2)"/>
    <rect x="-10" y="-362" width="20" height="20" fill="#cc3366" transform="rotate(333.9)"/>
    <rect x="-10" y="-362" width="20" height="20" fill="#ffcc00" transform="rotate(344.4)"/>
  </g>

  <!-- ingredient labels -->
  <g class="leaf-labels">
    <text class="leaf left" transform="rotate(85) translate(-370 0)">Rice Vinegar</text>
    <text class="leaf left" transform="rotate(88.5) translate(-370 0)">Balsamic Vinegar</text>
    <text class="leaf" transform="rotate(-87.7) translate(370 0)">Apple Cider Vinegar</text>
    <text class="leaf" transform="rotate(-79.6) translate(370 0)">Sumac</text>
    <text class="leaf" transform="rotate(-75.95) translate(370 0)">Zests</text>
    <text class="leaf" transform="rotate(-72.3) translate(370 0)">Lime</text>
    <text class="leaf" transform="rotate(-68.65) translate(370 0)">Lemon</text>
    <text class="leaf" transform="rotate(-65) translate(370 0)">Coriander</text>
    <text class="leaf" transform="rotate(-61.35) translate(370 0)">Celery</text>
    <text class="leaf" transform="rotate(-57.7) translate(370 0)">Tea</text>
    <text class="leaf" transform="rotate(-54.05) translate(370 0)">Sage</text>
    <text class="leaf" transform="rotate(-50.4) translate(370 0)">Oregano</text>
    <text class="leaf faint" transform="rotate(-46.75) translate(370 0)">Thyme</text>
    <text class="leaf" transform="rotate(-43.1) translate(370 0)">Rosemary</text>
    <text class="leaf" transform="rotate(-39.45) translate(370 0)">Bay Leaf</text>
    <text class="leaf" transform="rotate(-35.8) translate(370 0)">Fennel</text>
    <text class="leaf" transform="rotate(-32.15) translate(370 0)">Five Spice</text>
    <text class="leaf" transform="rotate(-28.5) translate(370 0)">Nutmeg</text>
    <text class="leaf" transform="rotate(-24.85) translate(370 0)">Turmeric</text>
    <text class="leaf" transform="rotate(-21.2) translate(370 0)">Star Anise</text>
    <text class="leaf" transform="rotate(-17.55) translate(370 0)">Cinnamin</text>
    <text class="leaf" transform="rotate(-13.9) translate(370 0)">Clove</text>
    <text class="leaf" transform="rotate(-10.25) translate(370 0)">Pecan</text>
    <text class="leaf" transform="rotate(-6.6) translate(370 0)">Coffee</text>
    <text class="leaf" transform="rotate(-2.95) translate(370 0)">Butter</text>
    <text class="leaf" transform="rotate(0.7) translate(370 0)">Fruit Juice</text>
    <text class="leaf" transform="rotate(4.35) translate(370 0)">Fruits</text>
    <text class="leaf" transform="rotate(8) translate(370 0)">Sauce/Ketchup</text>
    <text class="leaf" transform="rotate(14.9) translate(370 0)">Cola</text>
    <text class="leaf" transform="rotate(18.3) translate(370 0)">Agave Nectar</text>
    <text class="leaf" transform="rotate(21.8) translate(370 0)">Sugars</text>
    <text class="leaf" transform="rotate(31.9) translate(370 0)">Honey</text>
    <text class="leaf" transform="rotate(35.7) translate(370 0)">Molasses</text>
    <text class="leaf" transform="rotate(39) translate(370 0)">Maple Syrup</text>
    <text class="leaf" transform="rotate(56.6) translate(370 0)">Anchovies</text>
    <text class="leaf" transform="rotate(60) translate(370 0)">Garlic</text>
    <text class="leaf" transform="rotate(63.6) translate(370 0)">Sea Salt</text>
    <text class="leaf" transform="rotate(67) translate(370 0)">Kosher Salt</text>
    <text class="leaf" transform="rotate(84.5) translate(370 0)">Soy Sauce</text>
    <text class="leaf" transform="rotate(88) translate(370 0)">Fish Sauce</text>
    <text class="leaf left" transform="rotate(272) translate(-370 0)">Worcestershire</text>
    <text class="leaf left" transform="rotate(275.9) translate(-370 0)">Seasoning Sauce</text>
    <text class="leaf left" transform="rotate(287.1) translate(-370 0)">Phosphates</text>
    <text class="leaf left" transform="rotate(290.6) translate(-370 0)">Stocks</text>
    <text class="leaf left" transform="rotate(294.1) translate(-370 0)">Lard</text>
    <text class="leaf left" transform="rotate(297.7) translate(-370 0)">Yeastmite</text>
    <text class="leaf left" transform="rotate(301.4) translate(-370 0)">MSG</text>
    <text class="leaf left" transform="rotate(315.1) translate(-370 0)">Horseradish</text>
    <text class="leaf left" transform="rotate(318.7) translate(-370 0)">Wasabi</text>
    <text class="leaf left" transform="rotate(322.2) translate(-370 0)">Pepper</text>
    <text class="leaf left" transform="rotate(325.5) translate(-370 0)">Cumin</text>
    <text class="leaf left" transform="rotate(329) translate(-370 0)">Szechuan</text>
    <text class="leaf left" transform="rotate(332.6) translate(-370 0)">Onion</text>
    <text class="leaf left" transform="rotate(339.7) translate(-370 0)">Chipotle</text>
    <text class="leaf left" transform="rotate(343.2) translate(-370 0)">Jalapeno</text>
    <text class="leaf left" transform="rotate(346.7) translate(-370 0)">Hot Sauce</text>
    <text class="leaf left" transform="rotate(350.2) translate(-370 0)">Habanero</text>
    <text class="leaf left" transform="rotate(353.6) translate(-370 0)">Red Pepper</text>
    <text class="leaf left" transform="rotate(357) translate(-370 0)">Mustard</text>
    <text class="leaf left" transform="rotate(359.4) translate(-370 0)">Paprika</text>
    <text class="leaf left" transform="rotate(15) translate(-370 0)">Hard Woods</text>
    <text class="leaf left" transform="rotate(18.3) translate(-370 0)">Fruit Woods</text>
    <text class="leaf left" transform="rotate(21.8) translate(-370 0)">Charcoal</text>
    <text class="leaf left" transform="rotate(25.4) translate(-370 0)">Whiskey</text>
    <text class="leaf left" transform="rotate(28.9) translate(-370 0)">Bourbon</text>
    <text class="leaf left" transform="rotate(46.5) translate(-370 0)">Creosote</text>
    <text class="leaf left" transform="rotate(60.2) translate(-370 0)">Cocktail Bitters</text>
    <text class="leaf left" transform="rotate(63.9) translate(-370 0)">Citric Acid</text>
    <text class="leaf left" transform="rotate(74.4) translate(-370 0)">Tamarind</text>
  </g>

</g>
</svg>
</div>
</body>
</html>
```